American cannabis tech company business card design

Thrum.com is seeking a modern, professional, and brand-aligned business card that represents our company and its core values: Mission, Story, Values, and Impact. As an innovative cannabis company, we want a business card that is not only visually appealing but also serves as a representation of who we are and what we stand for.

Project Scope: Design a double-sided business card that integrates our brand identity and core values. Incorporate our key brand elements, ensuring a sleek and contemporary aesthetic. Visually reflect our core values (Mission, Story, Values, Impact) in a way that is engaging yet professional.

Target Market(s)

Vendors, third parties,

Contact Information for Business Card

Contact details (name, title, email, phone, website, etc.)

Font styles to use
Other font styles liked:
• Caslon, Centra

Colors

Designer to choose colors to be used in the design.

Requirements
Must have
• Thrum.com logo and branding A creative yet clean way to integrate our core values (Mission, Story, Values, Impact) Modern typography and a well-structured layout
Nice to have
• forest green, grey, white, black
Should not have
• references to marijuana, leafs, plants, or related product

```html
<!DOCTYPE html>
<html lang="en">
<head>
<meta charset="utf-8">
<title>Thrum.com Business Card</title>
<link rel="stylesheet" href="https://fonts.googleapis.com/css2?family=Urbanist:wght@400;500;700;800&display=swap">
<style>
  :root {
    --backdrop: #969696;
    --forest: #1b3320;
    --forest-deep: #17291b;
    --forest-light: #203a26;
    --kraft: #a88a61;
    --kraft-light: #ae9168;
    --ink-light: #d8ccc2;
    --rule: rgba(216, 204, 194, 0.45);
  }
  * { margin: 0; padding: 0; box-sizing: border-box; }
  html, body {
    width: 1200px;
    height: 1000px;
    overflow: hidden;
    background: var(--backdrop);
    font-family: "Urbanist", sans-serif;
  }
  .canvas {
    position: relative;
    width: 1200px;
    height: 1000px;
  }
  .card {
    position: absolute;
    left: 252px;
    width: 694px;
    height: 400px;
    border-radius: 24px;
    overflow: hidden;
  }
  .card--front {
    top: 60px;
    background: var(--forest);
  }
  .card--back {
    top: 490px;
    background: linear-gradient(135deg, var(--kraft-light), var(--kraft));
  }
  .front-pattern {
    position: absolute;
    inset: 0;
    background: linear-gradient(90deg, var(--forest-deep) 0%, var(--forest) 50%, var(--forest-light) 100%);
  }
  .front-wordmark {
    position: absolute;
    right: 78px;
    top: 262px;
    font-weight: 800;
    font-size: 34px;
    letter-spacing: 0.5px;
    color: var(--ink-light);
  }
  .person {
    position: absolute;
    left: 62px;
    top: 132px;
    color: var(--ink-light);
  }
  .person__name {
    font-weight: 700;
    font-size: 32px;
    line-height: 32px;
  }
  .person__title {
    margin-top: 14px;
    font-weight: 500;
    font-size: 21px;
  }
  .divider {
    position: absolute;
    left: 62px;
    right: 62px;
    top: 258px;
    height: 1px;
    background: var(--rule);
  }
  .contacts {
    position: absolute;
    left: 66px;
    top: 274px;
    list-style: none;
    color: var(--ink-light);
    font-weight: 500;
    font-size: 22px;
  }
  .contacts li {
    display: flex;
    align-items: center;
    height: 29px;
  }
  .contacts svg {
    width: 20px;
    height: 20px;
    margin-right: 14px;
    stroke: var(--ink-light);
    fill: none;
    stroke-width: 1.3;
  }
  .back-wordmark {
    position: absolute;
    right: 62px;
    top: 310px;
    font-weight: 800;
    font-size: 40px;
    letter-spacing: 0.5px;
    color: var(--ink-light);
  }
</style>
</head>
<body>
<main class="canvas">
  <section class="card card--front">
    <div class="front-pattern" role="img" aria-label="Repeating embossed brand monogram pattern in deep forest green"></div>
    <div class="front-wordmark">THRUM</div>
  </section>

  <section class="card card--back">
    <div class="person">
      <h1 class="person__name">Name<br>Surname</h1>
      <p class="person__title">Title</p>
    </div>
    <div class="divider"></div>
    <ul class="contacts">
      <li>
        <svg viewBox="0 0 20 20"><rect x="2" y="5" width="16" height="11"/><path d="M2 5l8 6 8-6"/></svg>
        name@thrum.com
      </li>
      <li>
        <svg viewBox="0 0 20 20"><rect x="6" y="2" width="8" height="16" rx="1.5"/><path d="M9 15.5h2"/></svg>
        405-555-0182
      </li>
      <li>
        <svg viewBox="0 0 20 20"><circle cx="10" cy="10" r="7.5"/><ellipse cx="10" cy="10" rx="3.5" ry="7.5"/><path d="M2.5 10h15M4 6h12M4 14h12"/></svg>
        thrum.com
      </li>
    </ul>
    <div class="back-wordmark">THRUM</div>
  </section>
</main>
</body>
</html>
```